Ecommerce site for Curtain Track Company

This is an ecommerce store design and will be based on the xcart ecommerce platform, attached is a design specification and all images to use in the design, you may use any other images you see fit.
This is a new Company so has no logo, if possible please create a logo but if not just use a text based logo in the design this maybe replaced later if required.
We only require a Home page design initially but will also need a category and product page design created, if you can do those also it would be an advantage.
IMPORTANT
We require all designs to be supplied as a full size JPG so we can see the design in detail as the pixel harbor previews are often too small.

```html
<!DOCTYPE html>
<html lang="en">
<head>
<meta charset="utf-8">
<title>Kestrel Rails – Curtain Tracks</title>
<link href="https://fonts.googleapis.com/css2?family=Arimo:wght@400;700&display=swap" rel="stylesheet">
<style>
:root{
  --page:#e9e9ea;
  --panel:#ffffff;
  --ink:#333333;
  --muted:#8a8a8a;
  --dark:#1e1e1e;
  --line:#dcdcdc;
  --accent:#f07a1a;
  --red:#d91e1e;
  --soft:#f3f3f3;
}
*{box-sizing:border-box;margin:0;padding:0}
html,body{width:943px;height:1200px;overflow:hidden}
body{position:relative;background:var(--page);font-family:"Arimo",Arial,sans-serif;color:var(--ink)}
.top-strip{position:absolute;left:0;top:0;width:943px;height:4px;background:#cfcfcf}
.header-band{position:absolute;left:0;top:4px;width:943px;height:162px;background:linear-gradient(#ffffff,#ececec)}
.sheet{position:absolute;left:44px;top:143px;width:857px;height:957px;background:var(--panel);box-shadow:0 0 6px rgba(0,0,0,.15)}
.brand{position:absolute;left:64px;top:66px;font-size:25px;font-weight:700;color:#555;letter-spacing:-.5px;white-space:nowrap}
.shipping{position:absolute;left:250px;top:87px;width:464px;height:37px;background:#fff;box-shadow:0 2px 3px rgba(0,0,0,.15)}
.shipping .tag{position:absolute;left:0;top:0;width:130px;height:37px;background:linear-gradient(var(--red),#a80f0f);color:#fff;font-size:14px;font-weight:700;line-height:37px;padding-left:8px;clip-path:polygon(0 0,88% 0,100% 50%,88% 100%,0 100%)}
.shipping .truck{position:absolute;left:137px;top:5px;width:55px;height:27px;background:linear-gradient(90deg,#f3b21a,#8a8f96);border-radius:3px}
.shipping .msg{position:absolute;left:202px;top:0;line-height:37px;font-size:14.5px;color:#222}
.cart{position:absolute;left:725px;top:25px;width:166px;height:104px;background:var(--soft);border:1px solid var(--line)}
.cart h2{position:absolute;right:8px;top:9px;font-size:11px;font-weight:700;color:#333}
.cart .basket{position:absolute;left:10px;top:25px;width:46px;height:40px}
.cart .items{position:absolute;right:24px;top:34px;font-size:9.5px;color:var(--muted)}
.cart .total{position:absolute;right:18px;top:52px;font-size:10px;font-weight:700;color:#666}
.cart .view{position:absolute;left:28px;top:73px;width:60px;height:20px;font-size:10px;font-weight:700;line-height:20px;text-align:center;color:#333;background:#fff;border:1px solid var(--line)}
.cart .checkout{position:absolute;left:92px;top:73px;width:60px;height:20px;font-size:10px;font-weight:700;line-height:20px;text-align:center;color:#fff;background:linear-gradient(#555,#111)}
.nav{position:absolute;left:44px;top:143px;width:857px;height:37px;background:linear-gradient(#3c3c3c,#111);display:flex}
.nav a{color:#fff;font-size:13px;text-decoration:none;line-height:37px;padding:0 15px;border-right:1px solid #555}
.search{position:absolute;left:728px;top:150px;width:157px;height:23px;background:#444;border:1px solid #666;color:#ccc;font-size:10.5px;line-height:21px;padding-left:8px}
.search svg{position:absolute;right:6px;top:4px}
.side-head{position:absolute;left:52px;width:185px;height:29px;background:linear-gradient(#3c3c3c,#111);color:#fff;font-size:12.5px;line-height:29px;padding-left:10px;border-radius:3px 3px 0 0}
.side-head::after,.cat li::after{content:"";position:absolute;right:12px;top:50%;width:14px;height:14px;margin-top:-7px;border-radius:50%}
.side-head::after{background:#555}
.cat{position:absolute;left:52px;top:237px;width:185px;list-style:none}
.cat li{position:relative;height:29px;border-bottom:1px solid #fff;background:linear-gradient(#f4f4f4,#e3e3e3);font-size:10.5px;line-height:29px;padding-left:10px;color:#777}
.cat li::after{background:#fff;border:1px solid #bbb}
.recent{position:absolute;left:52px;top:400px;width:185px;height:235px;border:1px solid var(--line);border-top:0}
.recent .item{position:absolute;left:10px;width:163px;height:70px;border-bottom:1px solid var(--line)}
.recent .thumb{position:absolute;left:0;top:0;width:69px;height:59px;background:#cfcfcf}
.recent .name{position:absolute;left:77px;top:14px;font-size:11.5px;font-weight:700;color:#777}
.hero{position:absolute;left:250px;top:207px;width:644px;height:247px;border:1px solid var(--line);padding:3px}
.hero div{width:100%;height:100%;background:linear-gradient(90deg,#263036 0%,#e7e4e0 20%,#f2f0ee 55%,#c9c5c0 78%,#2b3238 100%)}
.feature{position:absolute;top:464px;width:201px;height:64px;border:1px solid var(--line);background:linear-gradient(#fff,#f1f1f1);font-size:10px;font-weight:700;color:#222;line-height:14px;padding:14px 0 0 4px;letter-spacing:-.1px;white-space:nowrap}
.feature .art{position:absolute;right:2px;top:2px;width:46px;height:58px}
.welcome{position:absolute;left:250px;top:551px;font-size:18px;font-weight:400;color:#555}
.intro{position:absolute;left:250px;top:576px;width:620px;font-size:10.8px;line-height:15.5px;color:#999}
.featured{position:absolute;left:250px;top:703px;width:644px;height:35px;background:linear-gradient(#3c3c3c,#111);border-radius:3px;color:#fff;font-size:13px;line-height:35px;padding-left:22px}
.card{position:absolute;width:304px;height:130px;border:1px solid var(--line);background:linear-gradient(#fff,#efefef)}
.card h3{position:absolute;left:14px;top:11px;font-size:12px;font-weight:400;color:#222}
.card p{position:absolute;left:14px;top:29px;width:150px;font-size:10px;line-height:15px;color:#999}
.card .price{position:absolute;left:14px;top:64px;font-size:21px;color:var(--accent)}
.card .more{position:absolute;left:14px;top:96px;width:80px;height:20px;background:linear-gradient(#444,#111);color:#fff;font-size:9.5px;line-height:20px;text-align:center;border-radius:2px}
.card .photo{position:absolute;right:10px;top:7px;width:104px;height:109px;background:linear-gradient(135deg,#c9d25a,#9aa07a 50%,#6f7466)}
.footer{position:absolute;left:0;top:1100px;width:943px;height:100px;background:#1f1f1f}
.footer nav{position:absolute;left:53px;top:19px;font-size:10.5px;color:#bbb}
.footer nav span{color:#777;margin:0 4px}
.footer small{position:absolute;left:53px;top:42px;font-size:10.5px;color:#999}
.pay{position:absolute;top:14px;width:40px;height:26px;background:#e8e8e8;border-radius:3px;transform:rotate(-10deg)}
</style>
</head>
<body>
<div class="top-strip"></div>
<div class="header-band"></div>
<div class="sheet"></div>

<div class="brand">Kestrel Rails</div>

<div class="shipping">
  <div class="tag">FREE SHIPPING</div>
  <div class="truck" role="img" aria-label="Delivery truck illustration"></div>
  <div class="msg">Free UK delivery on orders over £100</div>
</div>

<div class="cart">
  <h2>MY SHOPPING CART</h2>
  <svg class="basket" viewBox="0 0 46 40" aria-hidden="true"><path d="M4 14h38l-5 22H9z" fill="#f3b21a" stroke="#c98a00"/><path d="M12 14l8-11M34 14l-8-11" stroke="#777" stroke-width="2" fill="none"/></svg>
  <div class="items">0 items</div>
  <div class="total">Total:$0.00</div>
  <div class="view">view cart</div>
  <div class="checkout">check out</div>
</div>

<nav class="nav">
  <a>HOME</a><a>ABOUT US</a><a>SERVICES</a><a>PRODUCTS</a><a>CONTACT US</a>
</nav>
<div class="search">Search
  <svg width="13" height="13" viewBox="0 0 13 13" aria-hidden="true"><circle cx="5" cy="5" r="3.8" stroke="#ddd" stroke-width="1.6" fill="none"/><path d="M8 8l4 4" stroke="#ddd" stroke-width="1.8"/></svg>
</div>

<div class="side-head" style="top:207px">CATEGORY</div>
<ul class="cat">
  <li>Quiet Glide Tracks</li>
  <li>Hand operated Tracks</li>
  <li>Cord operated Tracks</li>
  <li>Automated Tracks</li>
</ul>
<div class="side-head" style="top:370px">RECENTLY VIEWED</div>
<div class="recent">
  <div class="item" style="top:10px"><div class="thumb"></div><div class="name">Lorem ipsum</div></div>
  <div class="item" style="top:88px"><div class="thumb"></div><div class="name">Lorem ipsum</div></div>
  <div class="item" style="top:166px;border-bottom:0"><div class="thumb"></div><div class="name">Lorem ipsum</div></div>
</div>

<div class="hero"><div role="img" aria-label="Bright living room with sheer curtains on a ceiling track and lounge chairs"></div></div>

<div class="feature" style="left:250px">Over 20 years experience<br>measuring / making / fitting
  <div class="art" role="img" aria-label="Fitter measuring a window" style="background:linear-gradient(135deg,#f0c27a,#d8691c)"></div></div>
<div class="feature" style="left:473px">5 years guarantee on all<br>quiet glide products
  <svg class="art" viewBox="0 0 46 58" aria-hidden="true"><circle cx="23" cy="29" r="21" fill="#e9b312" stroke="#b88400" stroke-width="2"/></svg></div>
<div class="feature" style="left:695px;padding-top:8px">Friendly family run<br>business
  <div class="art" role="img" aria-label="Forklift carrying boxes" style="background:linear-gradient(135deg,#f4f4f4,#c8955a)"></div></div>

<h1 class="welcome">Welcome to Kestrel Rails</h1>
<p class="intro">Lorem ipsum dolor sit amet, consectetuer adipiscing elit. Aenean commodo ligula eget dolor. Aenean massa. Cum sociis natoque penatibus et magnis dis parturient montes, nascetur ridiculus mus. Donec quam felis, ultricies nec, pellentesque eu, pretium quis, sem. Nulla consequat massa quis enim. Donec pede justo, fringilla vel, aliquet nec, vulputate eget, arcu. In enim justo, rhoncus ut, imperdiet a, venenatis vitae, justo. Nullam dictum felis eu pede mollis pretium. Integer Lorem ipsum dolor sit amet, consectetuer adipiscing elit. Aenean commodo ligula eget dolor. Aenean massa. Cum sociis natoque penatibus et magnis dis parturient montes, nascetur ridiculus mus. Donec quam felis, ultricies nec, pellentesque eu, pretium quis, sem. Nulla consequat massa quis enim. Donec pede justo, fringilla vel, aliquet nec, vulputate eget, arcu. In enim justo,</p>

<div class="featured">FEATURED PRODUCTS</div>

<div class="card" style="left:250px;top:753px"><h3>PRODUCT NAME</h3><p>Lorem ipsum dolor sit amet, con-sectetuer adipiscing elit.</p><div class="price">£ 99.00</div><div class="more">MORE DETAILS</div><div class="photo" role="img" aria-label="Curtain track rods and cord"></div></div>
<div class="card" style="left:587px;top:753px"><h3>PRODUCT NAME</h3><p>Lorem ipsum dolor sit amet, con-sectetuer adipiscing elit.</p><div class="price">£ 99.00</div><div class="more">MORE DETAILS</div><div class="photo" role="img" aria-label="Curtain track rods and cord"></div></div>
<div class="card" style="left:250px;top:899px"><h3>PRODUCT NAME</h3><p>Lorem ipsum dolor sit amet, con-sectetuer adipiscing elit.</p><div class="price">£ 99.00</div><div class="more">MORE DETAILS</div><div class="photo" role="img" aria-label="Curtain track rods and cord"></div></div>
<div class="card" style="left:587px;top:899px"><h3>PRODUCT NAME</h3><p>Lorem ipsum dolor sit amet, con-sectetuer adipiscing elit.</p><div class="price">£ 99.00</div><div class="more">MORE DETAILS</div><div class="photo" role="img" aria-label="Curtain track rods and cord"></div></div>

<footer class="footer">
  <nav>Home<span>|</span>About Us<span>|</span>Contact Us<span>|</span>FAQ's<span>|</span>Delivery Terms<span>|</span>Articles<span>|</span>Sitemap<span>|</span>Terms &amp; Conditions<span>|</span>Privacy</nav>
  <small>© 2011 KestrelRails.com. All Rights Reserved.</small>
  <div class="pay" style="left:729px"></div>
  <div class="pay" style="left:788px"></div>
  <div class="pay" style="left:847px"></div>
</footer>
</body>
</html>
```